BRD business cards Dr. Martin Velk

I need a business card designed for our dental office. We are a "general dental" practice.
Looking for a clean, professional but not too fancy design with our logo and contact information required.
front of card is information/standard business card, backside is appt reminder with lines for date and time of appt
doctors name: Dr. Martin Velk DMD
office name: Velk Family Dental
address: 4827 E Tolland Ave Coral Springs, FL 33065
phone: 954-555-0173
Dentistry
Office name, Doctor name, address, phone number...etc
- White/off white base color, blue and or black lettering

```html
<!DOCTYPE html>
<html lang="en">
<head>
<meta charset="utf-8">
<title>Velk Family Dental – Business Card</title>
<link rel="stylesheet" href="https://fonts.googleapis.com/css2?family=Cinzel:wght@500&family=Roboto:wght@400;500&family=Tinos:wght@700&display=swap">
<style>
  :root {
    --backdrop: #2b2b2b;
    --card: #f1f1f1;
    --brand-blue: #124a8c;
    --ink-gray: #4a4f55;
    --white: #ffffff;
  }
  * { margin: 0; padding: 0; box-sizing: border-box; }
  html, body { width: 1200px; height: 1138px; overflow: hidden; }
  body { background: var(--backdrop); position: relative; font-family: "Roboto", Arial, sans-serif; }

  .card {
    position: absolute;
    left: 290px;
    width: 620px;
    height: 375px;
    background: var(--card);
    border-radius: 14px;
    overflow: hidden;
  }
  .card--front { top: 186px; }
  .card--back { top: 607px; }

  .brand-name {
    font-family: "Cinzel", "Times New Roman", serif;
    font-weight: 500;
    color: var(--ink-gray);
    letter-spacing: 1px;
    line-height: 1.1;
    text-transform: uppercase;
  }

  .front-lockup {
    position: absolute;
    left: 0; right: 0; top: 92px;
    display: flex; flex-direction: column; align-items: center;
  }
  .front-mark {
    width: 64px; height: 64px; border-radius: 50%;
    background: var(--brand-blue);
    margin-bottom: 34px;
  }
  .front-lockup .brand-name { font-size: 32px; text-align: center; }

  .back-brand {
    position: absolute; left: 28px; top: 40px;
    font-size: 28px;
  }

  .info-band {
    position: absolute; left: 0; right: 0; top: 121px; height: 216px;
    background: var(--brand-blue);
  }
  .band-disc {
    position: absolute; left: 316px; top: 97px;
    width: 270px; height: 260px; border-radius: 50%;
    background: var(--card);
  }

  .doctor-name {
    position: absolute; left: 28px; top: 171px;
    font-family: "Tinos", "Times New Roman", serif;
    font-weight: 700; font-size: 22px;
    color: var(--white);
  }
  .contact-list {
    position: absolute; left: 28px; top: 212px;
    list-style: none; color: var(--white);
    font-size: 15.5px; line-height: 24px;
  }
  .contact-list li { display: flex; align-items: flex-start; }
  .contact-list .icon { width: 14px; height: 14px; margin: 5px 12px 0 2px; flex: none; }
  .contact-phone { font-weight: 500; font-size: 16px; margin-bottom: 0; }
</style>
</head>
<body>
  <section class="card card--front" aria-label="Card front">
    <div class="front-lockup">
      <div class="front-mark"></div>
      <p class="brand-name">Velk Family<br>Dental</p>
    </div>
  </section>

  <section class="card card--back" aria-label="Card back">
    <p class="brand-name back-brand">Velk Family Dental</p>
    <div class="info-band"></div>
    <div class="band-disc"></div>
    <p class="doctor-name">Dr. Martin Velk DMD</p>
    <ul class="contact-list">
      <li class="contact-phone">
        <svg class="icon" viewBox="0 0 24 24" fill="#ffffff" aria-hidden="true"><path d="M6.6 10.8a15.1 15.1 0 0 0 6.6 6.6l2.2-2.2a1 1 0 0 1 1-.25 11.4 11.4 0 0 0 3.6.57 1 1 0 0 1 1 1V20a1 1 0 0 1-1 1A17 17 0 0 1 3 4a1 1 0 0 1 1-1h3.5a1 1 0 0 1 1 1c0 1.25.2 2.45.57 3.57a1 1 0 0 1-.25 1z"/></svg>
        954-555-0173
      </li>
      <li>
        <svg class="icon" viewBox="0 0 24 24" fill="#ffffff" aria-hidden="true"><path d="M12 2a7 7 0 0 0-7 7c0 5.2 7 13 7 13s7-7.8 7-13a7 7 0 0 0-7-7zm0 9.5A2.5 2.5 0 1 1 12 6.5a2.5 2.5 0 0 1 0 5z"/></svg>
        <span>4827 E Tolland Ave Coral<br>Springs, FL 33065</span>
      </li>
    </ul>
  </section>
</body>
</html>
```